Email Signature

Hello,

We need an editable file so that when new staff start or someone is promoted we can easily edit this file.

The previous designer has not kept the email signatures uniform they should all be as per Garth Lindqvist signature.

I also need the Tomas Pirelli changes as below -
Senior Mechanical Engineer
Email should be tomas.pirelli@vantoq.com.au

You can see the Dale Okonkwo file is different I need this the same as Garth Lindqvist format but with details changed.

Also need a new one with details as per below -
Hugh Fenwick
Commercial Manager
0417 352 609
hugh.fenwick@vantoq.com.au
www.vantoq.com.au

```html
<!DOCTYPE html>
<html lang="en">
<head>
<meta charset="utf-8">
<title>VANTOQ Email Signatures</title>
<link rel="stylesheet" href="https://fonts.googleapis.com/css2?family=Roboto:wght@700&family=Questrial&family=Righteous&display=swap">
<style>
  :root {
    --page-bg: #b09774;
    --card-bg: #ffffff;
    --brand-blue: #1e88d8;
    --sky-blue: #33c3f0;
    --leaf-green: #8cc63f;
    --ink: #222222;
    --ink-grey: #555a5f;
    --footer-text: #ffffff;
  }
  * { box-sizing: border-box; margin: 0; padding: 0; }
  html, body { width: 785px; height: 1200px; overflow: hidden; }
  body { background: var(--page-bg); position: relative; }

  .signature {
    position: absolute;
    left: var(--x); top: var(--y);
    width: var(--w); height: 200px;
    background: var(--card-bg);
    box-shadow: 0 4px 8px rgba(0,0,0,0.35);
    overflow: hidden;
  }
  .staff {
    position: absolute; left: 17px; top: 20px;
  }
  .staff-name {
    font-family: "Roboto", Arial, sans-serif;
    font-weight: 700; font-size: 26px; line-height: 1.1;
    color: var(--brand-blue);
    white-space: nowrap;
  }
  .staff-role {
    font-family: "Questrial", Arial, sans-serif;
    font-size: 15px; color: var(--ink); margin-top: 2px;
    white-space: nowrap;
  }
  .contact-list { list-style: none; margin-top: 16px; }
  .contact-item {
    display: flex; align-items: center; gap: 8px;
    font-family: "Questrial", Arial, sans-serif;
    font-size: 15.5px; color: var(--ink);
    height: 25px; white-space: nowrap;
  }
  .contact-icon { width: 18px; height: 18px; flex: none; }

  .brand {
    position: absolute; right: 16px; top: 26px; width: 318px;
    text-align: center;
  }
  .brand-name {
    font-family: "Righteous", "Arial Black", sans-serif;
    font-size: 72px; line-height: 1.05; color: var(--sky-blue);
    letter-spacing: 0;
    white-space: nowrap;
  }
  .brand-service {
    font-family: "Righteous", Arial, sans-serif;
    font-size: 21px; color: var(--ink-grey); margin-top: 4px;
    letter-spacing: 0.3px; white-space: nowrap;
  }
  .brand-division {
    display: flex; align-items: center; gap: 8px;
    font-family: "Righteous", Arial, sans-serif;
    font-size: 14px; color: var(--sky-blue); letter-spacing: 1px;
    white-space: nowrap;
  }
  .brand-division::before, .brand-division::after {
    content: ""; flex: 1; height: 2px; background: var(--sky-blue);
  }

  .signature-footer {
    position: absolute; left: 0; right: 0; bottom: 0; height: 21px;
    background: linear-gradient(180deg, #2aa8ec, var(--brand-blue));
    font-family: "Righteous", Arial, sans-serif;
    color: var(--footer-text);
  }
  .footer-address {
    position: absolute; left: 12px; top: 0; height: 21px;
    display: flex; align-items: center; gap: 3px;
    font-size: 13.5px; letter-spacing: 0.4px; white-space: nowrap;
  }
  .footer-address svg { width: 10px; height: 13px; }
  .footer-hotline {
    position: absolute; right: 0; top: 0; width: 36%; height: 21px;
    background: var(--leaf-green);
    clip-path: polygon(12px 0, 100% 0, 100% 100%, 0 100%);
    display: flex; align-items: center; justify-content: flex-end;
    padding-right: 16px; gap: 4px;
    font-size: 13.5px; letter-spacing: 1px; white-space: nowrap;
  }
  .footer-hotline .hotline-number { margin-right: 6px; }
  .social-dot {
    width: 11px; height: 11px; border-radius: 50%;
    background: var(--brand-blue); border: 1.5px solid #fff;
  }
</style>
</head>
<body>

<svg width="0" height="0" style="position:absolute" aria-hidden="true">
  <defs>
    <symbol id="icon-phone" viewBox="0 0 20 20">
      <circle cx="10" cy="10" r="10" fill="#1e88d8"/>
      <path d="M6.5 5h2l1 2.6-1.3 1a6 6 0 0 0 3.2 3.2l1-1.3 2.6 1v2c0 .8-.6 1.3-1.4 1.3A9 9 0 0 1 5.2 6.4C5.2 5.6 5.7 5 6.5 5z" fill="#fff"/>
    </symbol>
    <symbol id="icon-mail" viewBox="0 0 20 20">
      <circle cx="10" cy="10" r="10" fill="#1e88d8"/>
      <rect x="5" y="6.5" width="10" height="7" rx="1" fill="#fff"/>
      <path d="M5.5 7.2 10 10.5l4.5-3.3" fill="none" stroke="#1e88d8" stroke-width="1"/>
    </symbol>
    <symbol id="icon-web" viewBox="0 0 20 20">
      <circle cx="10" cy="10" r="10" fill="#1e88d8"/>
      <circle cx="10" cy="10" r="5.5" fill="none" stroke="#fff" stroke-width="1.4"/>
      <path d="M4.5 10h11M10 4.5c-2.4 3-2.4 8 0 11M10 4.5c2.4 3 2.4 8 0 11" fill="none" stroke="#fff" stroke-width="1.1"/>
    </symbol>
    <symbol id="icon-pin" viewBox="0 0 10 13">
      <path d="M5 0a4.5 4.5 0 0 0-4.5 4.5C.5 8 5 13 5 13s4.5-5 4.5-8.5A4.5 4.5 0 0 0 5 0zm0 6.3a1.8 1.8 0 1 1 0-3.6 1.8 1.8 0 0 1 0 3.6z" fill="#fff"/>
    </symbol>
  </defs>
</svg>

<section class="signature" style="--x:93px; --y:192px; --w:597px;">
  <div class="staff">
    <h2 class="staff-name">Hugh Fenwick</h2>
    <p class="staff-role">Commercial Manager</p>
    <ul class="contact-list">
      <li class="contact-item"><svg class="contact-icon"><use href="#icon-phone"/></svg>0417 352 609</li>
      <li class="contact-item"><svg class="contact-icon"><use href="#icon-mail"/></svg>hugh.fenwick@vantoq.com.au</li>
      <li class="contact-item"><svg class="contact-icon"><use href="#icon-web"/></svg>www.vantoq.com.au</li>
    </ul>
  </div>
  <div class="brand">
    <div class="brand-name">VANTOQ</div>
    <div class="brand-service">Commercial Air Conditioning</div>
    <div class="brand-division">A Division of Kessler Air</div>
  </div>
  <footer class="signature-footer">
    <div class="footer-address"><svg><use href="#icon-pin"/></svg>14/ 226 Harlow Street, Wendale QLD 4051</div>
    <div class="footer-hotline"><span class="hotline-number">1300 462 118</span><span class="social-dot"></span><span class="social-dot"></span><span class="social-dot"></span></div>
  </footer>
</section>

<section class="signature" style="--x:90px; --y:408px; --w:603px;">
  <div class="staff">
    <h2 class="staff-name">Tomas Pirelli</h2>
    <p class="staff-role">Senior Mechanical Engineer</p>
    <ul class="contact-list">
      <li class="contact-item"><svg class="contact-icon"><use href="#icon-phone"/></svg>0417 352 609</li>
      <li class="contact-item"><svg class="contact-icon"><use href="#icon-mail"/></svg>tomas.pirelli@vantoq.com.au</li>
      <li class="contact-item"><svg class="contact-icon"><use href="#icon-web"/></svg>www.vantoq.com.au</li>
    </ul>
  </div>
  <div class="brand">
    <div class="brand-name">VANTOQ</div>
    <div class="brand-service">Commercial Air Conditioning</div>
    <div class="brand-division">A Division of Kessler Air</div>
  </div>
  <footer class="signature-footer">
    <div class="footer-address"><svg><use href="#icon-pin"/></svg>14/ 226 Harlow Street, Wendale QLD 4051</div>
    <div class="footer-hotline"><span class="hotline-number">1300 462 118</span><span class="social-dot"></span><span class="social-dot"></span><span class="social-dot"></span></div>
  </footer>
</section>

<section class="signature" style="--x:92px; --y:628px; --w:600px;">
  <div class="staff">
    <h2 class="staff-name">Dale Okonkwo</h2>
    <p class="staff-role">Director</p>
    <ul class="contact-list">
      <li class="contact-item"><svg class="contact-icon"><use href="#icon-phone"/></svg>0438 615 270</li>
      <li class="contact-item"><svg class="contact-icon"><use href="#icon-mail"/></svg>dale.okonkwo@vantoq.com.au</li>
      <li class="contact-item"><svg class="contact-icon"><use href="#icon-web"/></svg>www.vantoq.com.au</li>
    </ul>
  </div>
  <div class="brand">
    <div class="brand-name">VANTOQ</div>
    <div class="brand-service">Commercial Air Conditioning</div>
    <div class="brand-division">A Division of Kessler Air</div>
  </div>
  <footer class="signature-footer">
    <div class="footer-address"><svg><use href="#icon-pin"/></svg>14/ 226 Harlow Street, Wendale QLD 4051</div>
    <div class="footer-hotline"><span class="hotline-number">1300 462 118</span><span class="social-dot"></span><span class="social-dot"></span><span class="social-dot"></span></div>
  </footer>
</section>

<section class="signature" style="--x:86px; --y:864px; --w:613px;">
  <div class="staff">
    <h2 class="staff-name">Garth Lindqvist</h2>
    <p class="staff-role">Site Project Manager</p>
    <ul class="contact-list">
      <li class="contact-item"><svg class="contact-icon"><use href="#icon-phone"/></svg>0455 903 164</li>
      <li class="contact-item"><svg class="contact-icon"><use href="#icon-mail"/></svg>garth.lindqvist@vantoq.com.au</li>
      <li class="contact-item"><svg class="contact-icon"><use href="#icon-web"/></svg>www.vantoq.com.au</li>
    </ul>
  </div>
  <div class="brand">
    <div class="brand-name">VANTOQ</div>
    <div class="brand-service">Commercial Air Conditioning</div>
    <div class="brand-division">A Division of Kessler Air</div>
  </div>
  <footer class="signature-footer">
    <div class="footer-address"><svg><use href="#icon-pin"/></svg>14/ 226 Harlow Street, Wendale QLD 4051</div>
    <div class="footer-hotline"><span class="hotline-number">1300 462 118</span><span class="social-dot"></span><span class="social-dot"></span><span class="social-dot"></span></div>
  </footer>
</section>

</body>
</html>
```